Frank Frenzy Feast - Team Eating Comp

Design a fun/ vibrant/ edgy/ funny/ eye catching poster for our upcoming hotdog eating challenge. We are a grundgy whiskey/ burger bar on the Sunshine Coast. We have previously done hotdog eating comps and this year will be a hybrid model. I have attached an old tshirt design, this time more pop art in the design.

Info for the poster :
- teams of 2
- can you finish 14 hotdogs between you in 10min?
- $35 to enter (refunded if you successfully complete the challenge)
- prize if you successfully complete challenge
- 29th July 2023
- 12pm-5pm
Come down to Rusty Tobs Pelicanbay for the challenge - one day only!!

rustytobspelicanbay.example

Target Market(s)

Sunshine Coast locals. Food Competitors.

Industry/Entity Type

Bar and Restaurant

Font styles to use
Other font styles liked:
• Veneer

Colors
FFF300
FFF600
FEFA6F
FFFEC7
FFFEE8
F0912C
F2A743
F7CA91
FBE8D2
FDF5EE
EE7325
F08F49
F5BC92
FAE3D3
FDF4ED
EB3D1F
EC4F4E
F09395
F8D3D4
FCEDEE

```html
<!DOCTYPE html>
<html lang="en">
<head>
<meta charset="utf-8">
<title>Frank Frenzy Feast – Team Eating Comp</title>
<link rel="stylesheet" href="https://fonts.googleapis.com/css2?family=Anton&family=Oswald:wght@500;600&display=swap">
<style>
  :root{
    --stage:#c9cdcf;
    --green-top:#a9d437;
    --green-mid:#8dc63f;
    --green-low:#9ccd3a;
    --ink:#252523;
    --white:#ffffff;
    --sausage:#eb3d1f;
    --sausage-soft:#ec4f4e;
    --bun:#f2a743;
    --bun-deep:#f0912c;
  }
  *{margin:0;padding:0;box-sizing:border-box}
  html,body{width:1200px;height:1200px;overflow:hidden;background:var(--stage)}
  .poster{
    position:absolute;left:247px;top:100px;width:707px;height:999px;
    background:
      radial-gradient(ellipse 70% 45% at 50% 52%,rgba(180,222,70,.55) 0%,rgba(180,222,70,0) 100%),
      linear-gradient(180deg,var(--green-top) 0%,var(--green-mid) 55%,var(--green-low) 100%);
    color:var(--ink);font-family:"Oswald",sans-serif;overflow:hidden;
  }
  .headline{
    position:absolute;left:0;right:0;top:31px;text-align:center;
    font-family:"Anton",sans-serif;font-weight:400;font-size:53px;line-height:82px;
    letter-spacing:2px;white-space:nowrap;
  }
  .headline .time{color:var(--white);font-size:55px;margin-left:10px}
  .illustration{
    position:absolute;left:78px;top:292px;width:570px;height:372px;
    border-radius:36px;
    background:linear-gradient(90deg,var(--bun) 0%,var(--sausage) 28%,var(--bun-deep) 50%,var(--sausage) 72%,var(--bun) 100%);
  }
  .burst{position:absolute;left:262px;top:223px;width:193px;height:161px}
  .event-date{
    position:absolute;left:0;right:0;top:680px;text-align:center;
    font-weight:600;font-size:45px;line-height:60px;letter-spacing:.5px;white-space:nowrap;
  }
  .terms{
    position:absolute;left:0;right:0;top:753px;text-align:center;
    font-weight:500;font-size:18.5px;line-height:30px;white-space:nowrap;
  }
  .invite{
    position:absolute;left:0;right:0;top:820px;text-align:center;
    font-weight:600;font-size:26px;line-height:48px;white-space:nowrap;
  }
  .invite .rule{display:inline-block;width:66px;height:2px;background:var(--ink);vertical-align:middle;margin:0 14px}
  .invite .highlight{color:var(--white);font-size:30px}
  .brand{
    position:absolute;left:45px;top:942px;font-weight:600;font-size:16px;letter-spacing:1px;
    display:flex;align-items:center;gap:6px;
  }
  .brand .dot{width:10px;height:10px;border-radius:50%;background:var(--ink)}
  .website{position:absolute;right:44px;top:943px;font-weight:500;font-size:17px}
</style>
</head>
<body>
<main class="poster">
  <h1 class="headline">CAN YOU FINISH 14 HOTDOGS<br>BETWEEN YOU IN <span class="time">10MIN?</span></h1>

  <div class="illustration" role="img" aria-label="Two cartoon hotdog characters with mustard fist-bumping"></div>

  <svg class="burst" viewBox="0 0 193 161">
    <polygon points="100,10 112,42 146,20 138,56 180,58 148,82 172,112 132,110 136,150 104,126 88,156 74,122 40,142 48,108 12,104 42,80 16,52 56,52 50,18 80,42"
      fill="#ffffff" stroke="#252523" stroke-width="2"/>
    <text x="84" y="82" text-anchor="middle" font-family="Oswald, sans-serif" font-weight="600" font-size="24" fill="#252523">TEAM</text>
    <text x="90" y="110" text-anchor="middle" font-family="Oswald, sans-serif" font-weight="600" font-size="24" fill="#252523">OF</text>
    <text x="128" y="114" text-anchor="middle" font-family="Anton, sans-serif" font-size="54" fill="#252523">2</text>
  </svg>

  <p class="event-date">29th JULY 2023 at 12PM-5PM</p>

  <p class="terms">•$35 to enter (refunded if you successfully complete the challenge)•<br>•prize if you successfully complete challenge•</p>

  <p class="invite"><span class="rule"></span>Come down to Rusty Tobs Pelicanbay<span class="rule"></span><br>for the challenge—<span class="highlight">one day only!!</span></p>

  <div class="brand"><span>RUSTY TOBS</span><span class="dot"></span></div>
  <p class="website">rustytobspelicanbay.example</p>
</main>
</body>
</html>
```